Automotive component supplier needs a business card design

We need a business card design for our company called Velmar Global Components Ltd based in the UK. We are a supplier of interior and exterior components to premium car manufacturers such as Corvane Hale, Durrant Fyfe, Maxtorn and Valdessimo. We would like to see a modern business card design that uses the colour blue.

Target Market(s)

Premium automotive car manufacturers.

Industry/Entity Type

Automotive

Contact Information for Business Card

Company Name : Velmar Global Components Limited
Address: 17 Tamsey Yard, Upper Drisk, Warwick, CV31 8RJ, United Kingdom
Web Address : www.velmarparts-example.co.uk

Font styles to use
Other font styles liked:
• Helvetica

Colors
3176b5
0255a3
85acd3
cfdeed
cee9f5
85cae6
34a6d7
0692cd
9bcb3c

Requirements
Must have
• Clear company logo and a mixture of blue colours.
Nice to have
• A high quality modern image.
Should not have
• Multiple colours.

```html
<!DOCTYPE html>
<html lang="en">
<head>
<meta charset="utf-8">
<title>Velmar Global Components – Business Card</title>
<link rel="stylesheet" href="https://fonts.googleapis.com/css2?family=Open+Sans:wght@400;600;700&display=swap">
<style>
  :root {
    --page-bg: #eef1f4;
    --brand-blue: #0692cd;
    --brand-cyan: #34a6d7;
    --brand-green: #9bcb3c;
    --card-black: #121314;
    --white: #ffffff;
    --soft-white: #e9eef2;
  }
  * { box-sizing: border-box; margin: 0; padding: 0; }
  html, body {
    width: 1200px; height: 900px; overflow: hidden;
    background: var(--page-bg);
    font-family: "Open Sans", Helvetica, Arial, sans-serif;
  }
  .canvas { position: relative; width: 1200px; height: 900px; }

  .card {
    position: absolute; width: 560px; height: 320px;
    border-radius: 4px; overflow: hidden;
    box-shadow: 0 12px 30px rgba(0,0,0,.18);
  }

  /* Front */
  .card-front {
    left: 110px; top: 120px;
    background: var(--brand-blue);
    display: flex; align-items: center; justify-content: center;
  }
  .wordmark { text-align: center; color: var(--white); }
  .wordmark-name {
    display: flex; align-items: center; justify-content: center; gap: 12px;
    font-weight: 700; font-size: 54px; letter-spacing: 2px; line-height: 1;
  }
  .wordmark-dot {
    width: 16px; height: 16px; border-radius: 50%; background: currentColor;
  }
  .wordmark-sub {
    font-weight: 700; font-size: 15px; letter-spacing: 3px; margin-top: 8px;
  }

  /* Back */
  .card-back { left: 530px; top: 460px; background: var(--card-black); }

  .accent-line {
    position: absolute; left: 0; right: 0; bottom: 66px; height: 4px;
    background: var(--brand-green);
  }
  .footer-band {
    position: absolute; left: 0; right: 0; bottom: 0; height: 60px;
    background: var(--brand-blue);
  }

  .back-logo {
    position: absolute; right: 30px; top: 34px; color: var(--brand-blue);
    text-align: left;
  }
  .back-logo .wordmark-name { font-size: 40px; justify-content: flex-start; gap: 9px; }
  .back-logo .wordmark-dot { width: 12px; height: 12px; }
  .back-logo .wordmark-sub { font-size: 11px; letter-spacing: 2px; margin-top: 6px; }

  .holder { position: absolute; left: 30px; top: 34px; }
  .holder-name { color: var(--brand-cyan); font-weight: 600; font-size: 20px; }
  .holder-role { color: var(--white); font-size: 14px; margin-top: 2px; }

  .contact-list {
    position: absolute; left: 30px; top: 112px; list-style: none;
    color: var(--soft-white); font-size: 15px; line-height: 22px;
  }
  .contact-list li { display: flex; align-items: center; gap: 10px; }
  .contact-list svg { width: 13px; height: 13px; flex: none; fill: var(--brand-cyan); }

  .address {
    position: absolute; left: 30px; top: 192px;
    color: var(--soft-white); font-size: 15px; line-height: 22px; font-style: normal;
  }
  .website {
    position: absolute; right: 26px; bottom: 20px;
    color: var(--white); font-size: 13px;
  }
</style>
</head>
<body>
<main class="canvas">

  <section class="card card-front" aria-label="Business card front">
    <div class="wordmark">
      <div class="wordmark-name"><span class="wordmark-dot"></span>VELMAR</div>
      <div class="wordmark-sub">GLOBAL COMPONENTS</div>
    </div>
  </section>

  <section class="card card-back" aria-label="Business card back">
    <div class="accent-line"></div>
    <div class="footer-band"></div>

    <div class="holder">
      <div class="holder-name">Dorian Kellaway</div>
      <div class="holder-role">Managing Director</div>
    </div>

    <div class="back-logo">
      <div class="wordmark-name"><span class="wordmark-dot"></span>VELMAR</div>
      <div class="wordmark-sub">GLOBAL COMPONENTS</div>
    </div>

    <ul class="contact-list">
      <li><svg viewBox="0 0 16 16"><path d="M3 1h3l1 4-2 1c1 2 3 4 5 5l1-2 4 1v3c0 1-1 2-2 2C7 15 1 9 1 3c0-1 1-2 2-2z"/></svg>(044) 208 513 774</li>
      <li><svg viewBox="0 0 16 16"><path d="M4 0h8c1 0 1 1 1 1v14s0 1-1 1H4s-1 0-1-1V1s0-1 1-1zm1 2v10h6V2zm3 11a1 1 0 100 2 1 1 0 000-2z"/></svg>(044)790315462</li>
      <li><svg viewBox="0 0 16 16"><path d="M0 3h16v1L8 9 0 4zm0 3l8 5 8-5v7H0z"/></svg>info@velmar-example.co.uk</li>
    </ul>

    <address class="address">
      17 Tamsey Yard, Upper Drisk,<br>
      Warwick, CV31 8RJ, United Kingdom
    </address>

    <div class="website">www.velmarparts-example.co.uk</div>
  </section>

</main>
</body>
</html>
```